TalkBridge - Language Coaching Services

Sleek, innovative, trendy design for Language Coaching business.

TalkBridge is a new UK based company that provides Language Coaching services. We offer highly personalized on-line and face to face language courses. We also impart learning techniques workshops based on the latest neuroscience research for second-language acquisition.

Target Market(s)

Industry/Entity Type

Consulting

Contact Information for Business Card

TalkBridge
ElenaVT@talkbridge-demo.co.uk
TalkBridge-demo.co.uk
London, UK

Font styles to use
Sans Serif

```html
<!DOCTYPE html>
<html lang="en">
<head>
<meta charset="utf-8">
<title>TalkBridge – Business Card</title>
<link rel="stylesheet" href="https://fonts.googleapis.com/css2?family=Ubuntu:wght@400;500;700&display=swap">
<style>
  :root {
    --backdrop: #555555;
    --card: #231f20;
    --brand-blue: #0b8ecb;
    --brand-blue-deep: #1a6fa3;
    --text-light: #f2f2f2;
  }
  * { margin: 0; padding: 0; box-sizing: border-box; }
  html, body {
    width: 1200px; height: 900px; overflow: hidden;
    background: var(--backdrop);
    font-family: "Ubuntu", sans-serif;
  }
  .canvas { position: relative; width: 1200px; height: 900px; }
  .card {
    position: absolute; top: 108px;
    width: 391px; height: 686px;
    background: var(--card);
    overflow: hidden;
  }
  .card--front { left: 168px; }
  .card--back { left: 641px; }

  /* front */
  .front-mark {
    position: absolute; left: 136px; top: 261px;
    width: 118px; height: 118px;
  }
  .front-wordmark {
    position: absolute; left: 0; right: 0; top: 385px;
    text-align: center;
    font-size: 42px; font-weight: 500; letter-spacing: 1px;
    color: var(--brand-blue);
  }
  .front-url {
    position: absolute; left: 0; right: 0; top: 632px;
    text-align: center;
    font-size: 19px; color: var(--text-light); letter-spacing: 0.3px;
  }

  /* back */
  .back-wordmark {
    position: absolute; left: 43px; top: 57px;
    font-size: 36px; font-weight: 500; letter-spacing: 1px;
    color: var(--brand-blue);
  }
  .back-ring {
    position: absolute; left: 136px; top: 120px;
    width: 320px; height: 330px;
  }
  .contact {
    position: absolute; left: 44px; top: 455px;
    color: var(--text-light);
  }
  .contact__name {
    font-size: 20px; font-weight: 700; color: var(--brand-blue);
    margin-bottom: 12px;
  }
  .contact__list { list-style: none; }
  .contact__item {
    display: flex; align-items: flex-start;
    font-size: 17px; line-height: 29px;
  }
  .contact__icon {
    width: 20px; height: 20px; margin: 4px 12px 0 0; flex: none;
    fill: var(--brand-blue);
  }
  .back-rule {
    position: absolute; left: 25px; right: 25px; top: 649px;
    height: 3px; background: var(--brand-blue);
  }
</style>
</head>
<body>
<main class="canvas">

  <section class="card card--front">
    <svg class="front-mark" viewBox="0 0 118 118" aria-hidden="true">
      <circle cx="59" cy="59" r="55" fill="none" stroke="var(--brand-blue)" stroke-width="7"/>
    </svg>
    <div class="front-wordmark">TALKBRIDGE</div>
    <div class="front-url">www.talkbridge-demo.co.uk</div>
  </section>

  <section class="card card--back">
    <div class="back-wordmark">TALKBRIDGE</div>
    <svg class="back-ring" viewBox="0 0 320 330" aria-hidden="true">
      <circle cx="270" cy="165" r="130" fill="none" stroke="var(--brand-blue)" stroke-width="13"/>
    </svg>

    <div class="contact">
      <div class="contact__name">TalkBridge</div>
      <ul class="contact__list">
        <li class="contact__item">
          <svg class="contact__icon" viewBox="0 0 24 24" aria-hidden="true"><path d="M6.6 10.8a15.1 15.1 0 0 0 6.6 6.6l2.2-2.2c.3-.3.7-.4 1-.2 1.1.4 2.3.6 3.6.6.6 0 1 .4 1 1V20c0 .6-.4 1-1 1A17 17 0 0 1 3 4c0-.6.4-1 1-1h3.5c.6 0 1 .4 1 1 0 1.3.2 2.5.6 3.6.1.3 0 .7-.2 1z"/></svg>
          <span>+44 1632 960718</span>
        </li>
        <li class="contact__item">
          <svg class="contact__icon" viewBox="0 0 24 24" aria-hidden="true"><path d="M2 5h20v14H2z M3.5 6.5 12 13l8.5-6.5" fill="var(--brand-blue)" stroke="var(--card)" stroke-width="1.5"/></svg>
          <span>ElenaVT@talkbridge-demo.co.uk</span>
        </li>
        <li class="contact__item">
          <svg class="contact__icon" viewBox="0 0 24 24" aria-hidden="true"><circle cx="12" cy="12" r="10"/><path d="M2 12h20M12 2c3 3 3 17 0 20M12 2c-3 3-3 17 0 20M4 7h16M4 17h16" fill="none" stroke="var(--card)" stroke-width="1.2"/></svg>
          <span>www.talkbridge-demo.co.uk</span>
        </li>
        <li class="contact__item">
          <svg class="contact__icon" viewBox="0 0 24 24" aria-hidden="true"><path d="M12 2a7 7 0 0 0-7 7c0 5.2 7 13 7 13s7-7.8 7-13a7 7 0 0 0-7-7zm0 9.5A2.5 2.5 0 1 1 12 6.5a2.5 2.5 0 0 1 0 5z"/></svg>
          <span>14 Harbour Lane, TN21 4QX,<br>London, UK</span>
        </li>
      </ul>
    </div>
    <div class="back-rule"></div>
  </section>

</main>
</body>
</html>
```